New Dental Office Needs an Attractive and user friendly Website Designed

I need a website for a new dental office. The Name is Maplecrest Dentistry. I would like a Modern design with a user friendly interface and usability.
I would like a landing page, a page that lists the services we offer: Cosmetic Dentistry, Implants, Dental Hygiene, Emergency Services, Restorations, Dentures
Target Market(s)
Mid to upper class
Industry/Entity Type
Dentistry
Coding
Coded - Design and coding required
Number of Pages Required
1 page
Requirements
Must have
- Landing page that has a scheduling option, Procedures, operating hours, and contact us info
Nice to have
- Appealing design, Soft comforting colors. Easy to navigate page, Modern and professional.

```html
<!DOCTYPE html>
<html lang="en">
<head>
<meta charset="utf-8">
<title>Maplecrest Dentistry</title>
<link rel="stylesheet" href="https://fonts.googleapis.com/css2?family=Urbanist:wght@400;500;600;700&display=swap">
<style>
:root{
  --blue:#1e88e5;
  --blue-dark:#1671c4;
  --green:#3ccb7f;
  --ink:#1b1b1f;
  --muted:#4a4d55;
  --soft:#eef6fd;
  --line:#d8dde4;
  --peach:#f3ddd3;
  --star:#f5a623;
  --teal:#2ba3b6;
}
*{box-sizing:border-box;margin:0;padding:0}
html,body{width:1200px;height:5396px;overflow:hidden}
body{position:relative;background:#fff;font-family:"Urbanist",sans-serif;color:var(--ink)}
.abs{position:absolute}
.ph{position:absolute}
/* header */
.brand{position:absolute;left:79px;top:38px;font-size:40px;font-weight:600;color:var(--ink);line-height:1}
.brand small{display:block;font-size:18px;letter-spacing:7px;margin-top:6px;font-weight:600}
.nav{position:absolute;left:548px;top:56px;display:flex;gap:18px;font-size:19px;font-weight:500}
.nav a{color:var(--ink);text-decoration:none}
.nav a.active{color:var(--blue)}
.book{position:absolute;left:956px;top:0;width:161px;height:135px;background:var(--blue);color:#fff;font-size:19px;font-weight:600;display:flex;align-items:center;justify-content:center}
/* hero */
.hero-photo{left:0;top:135px;width:1200px;height:835px;background:linear-gradient(160deg,#dde7f1 0%,#b9cde3 40%,#8aa9d0 70%,#e6edf5 100%);clip-path:polygon(0 0,100% 0,100% 88%,50% 100%,0 88%)}
.hero-accent{left:77px;top:698px;width:40px;height:280px;background:var(--peach)}
.hero-card{left:110px;top:658px;width:463px;height:479px;background:#fff;box-shadow:0 6px 18px rgba(0,0,0,.12);text-align:center;padding:70px 40px 0}
.hero-card h1{font-size:33px;font-weight:600}
.hero-card h2{font-size:25px;font-weight:500;margin-top:18px}
.hero-card p{font-size:19px;line-height:23px;margin-top:24px;color:var(--ink)}
.btn-green{background:var(--green);color:#fff;font-weight:600;border-radius:40px;display:flex;align-items:center;justify-content:center}
.hero-card .btn-green{position:absolute;left:125px;top:338px;width:213px;height:60px;font-size:20px}
/* shared headings */
.label{font-size:18px;font-weight:500}
.h2{font-size:26px;font-weight:700;line-height:32px}
.body{font-size:18px;line-height:23px;color:var(--muted)}
.center{text-align:center;left:0;width:1200px}
/* about */
.about-img{border-radius:2px}
/* services */
.services{left:0;top:1837px;width:1200px;height:565px;background:var(--soft)}
.svc{position:absolute;width:300px;display:flex;gap:12px}
.svc svg{flex:none}
.svc h4{font-size:14px;font-weight:600}
.svc p{font-size:13px;line-height:16px;color:var(--muted);margin-top:3px}
/* why */
.why-card{position:absolute;top:2702px;width:336px;height:277px;border:1px solid var(--line);padding:70px 26px 0}
.why-card.first{box-shadow:0 3px 8px rgba(0,0,0,.12)}
.why-card h3{color:var(--blue);font-size:20px;font-weight:700}
.why-card h5{font-size:15px;font-weight:500;margin-top:6px}
.why-card p{font-size:14px;line-height:20px;color:var(--muted);margin-top:12px}
/* testimonials */
.tcard{position:absolute;border:2px solid #9fc8ef;border-radius:8px;background:#fff;text-align:center}
.tcard .who{position:absolute;display:flex;align-items:center;text-align:left}
.avatar{border-radius:50%;background:linear-gradient(135deg,#6b5a48,#b99a7c)}
.stars{color:var(--star);letter-spacing:2px}
.dots{left:517px;top:3670px;display:flex;gap:13px}
.dots span{width:16px;height:16px;border-radius:50%;background:#d6dbe2}
.dots span.on{background:var(--blue)}
/* info band */
.map{left:469px;top:3760px;width:731px;height:552px;background:linear-gradient(135deg,#e9e4dc,#d9d8cf 50%,#cfe0c6 80%,#e6e1d8)}
.info{left:0;top:3760px;width:552px;height:552px;background:var(--blue);clip-path:polygon(0 0,100% 0,85% 100%,0 100%);color:#fff;padding:42px 0 0 83px}
.info h3{font-size:28px;font-weight:600;display:flex;align-items:center;gap:14px}
.info ul{margin:14px 0 0 10px;font-size:20px;line-height:27px;list-style:disc;padding-left:14px}
.info .addr{font-size:19px;line-height:28px}
/* contact */
.bottom-band{left:0;top:4790px;width:1200px;height:606px;background:linear-gradient(180deg,var(--teal) 0%,#2196d8 45%,var(--blue) 100%)}
.contact-card{left:90px;top:4454px;width:1020px;height:566px;background:#fff;box-shadow:0 4px 16px rgba(0,0,0,.1)}
.contact-panel{left:90px;top:4454px;width:420px;height:566px;background:var(--blue);color:#fff;padding:42px 0 0 34px}
.contact-panel h3{font-size:26px;font-weight:600}
.contact-panel .sub{font-size:15px;color:#cfe4f8;margin-top:16px}
.cline{position:absolute;left:34px;display:flex;align-items:center;gap:20px;font-size:14px}
.soc{position:absolute;top:506px;width:26px;height:26px;border-radius:50%;background:#111}
.field{position:absolute;width:240px;border-bottom:1px solid #bfc5cc;padding-bottom:8px}
.field label{display:block;font-size:11px;font-weight:600;color:#555}
.field span{display:block;font-size:13px;color:#777;margin-top:10px;height:16px}
/* footer */
.fline{left:73px;top:5066px;width:1044px;height:1px;background:rgba(255,255,255,.5)}
.fcol{position:absolute;top:5112px;color:#fff;font-size:13px}
.fcol h6{font-size:14px;font-weight:500;margin-bottom:22px}
.fcol li{list-style:none;margin-bottom:25px}
.news{left:860px;top:5100px;width:250px;height:160px;background:var(--green);border-radius:4px;padding:16px 12px;color:#fff}
.news h6{font-size:15px;font-weight:600}
.news .form{display:flex;margin-top:16px;height:32px}
.news .form span{flex:1;background:#fff;color:#999;font-size:10px;padding:10px 8px}
.news .form b{width:82px;background:var(--blue-dark);font-size:10px;font-weight:600;display:flex;align-items:center;justify-content:center}
.news p{font-size:10px;margin-top:14px;line-height:13px;color:#e4fbef}
.copy{top:5332px;color:#fff;font-size:13px}
</style>
</head>
<body>

<header>
  <div class="brand">Maplecrest<small>DENTISTRY</small></div>
  <nav class="nav">
    <a class="active" href="#">Home</a><a href="#">About</a><a href="#">Services</a><a href="#">Why Us</a><a href="#">Contact</a>
  </nav>
  <div class="book">Book Now</div>
</header>

<section class="hero">
  <div class="ph hero-photo" role="img" aria-label="Photo of two dentists examining a smiling patient in a dental chair"></div>
  <div class="ph hero-accent"></div>
  <div class="abs hero-card">
    <h1>Maplecrest Dentistry</h1>
    <h2>Where Your Smile Feels at Home</h2>
    <p>Discover gentle, personalized dental care in a modern and calming environment. Our experienced team is here to help you achieve the healthy, confident smile you deserve.</p>
    <div class="btn-green">Get Started</div>
  </div>
</section>

<section class="about">
  <div class="abs label" style="left:75px;top:1315px">About Us</div>
  <h2 class="abs h2" style="left:75px;top:1360px;width:520px">Exceptional Dental Care in a Comfortable and Professional Environment</h2>
  <p class="abs body" style="left:75px;top:1447px;width:510px;color:var(--ink)">At Maplecrest Dentistry, we are committed to providing high-quality dental care tailored to each patient's needs. Our modern clinic combines advanced technology, experienced professionals, and a warm, welcoming atmosphere to ensure your comfort at every visit. We believe that a healthy smile is the foundation of confidence and overall well-being — and we're here to help you achieve it.</p>
  <div class="ph about-img" style="left:604px;top:1214px;width:244px;height:244px;background:linear-gradient(135deg,#e8edf2,#b7c6d6)" role="img" aria-label="Photo of a dentist showing a patient results on a tablet"></div>
  <div class="ph about-img" style="left:604px;top:1433px;width:244px;height:300px;background:linear-gradient(135deg,#f0f3f6,#9ab7dc 70%,#3c78c8)" role="img" aria-label="Photo of a dentist checking a patient's teeth"></div>
  <div class="ph about-img" style="left:873px;top:1354px;width:244px;height:242px;background:linear-gradient(135deg,#eef1f4,#c4d2e0 60%,#8fa9c4)" role="img" aria-label="Photo of a dentist talking with a patient in the chair"></div>
</section>

<section>
  <div class="ph services"></div>
  <div class="ph" style="left:55px;top:1895px;width:360px;height:470px;background:linear-gradient(180deg,#dfe9f3,#f5f8fb)" role="img" aria-label="Photo of a smiling dentist holding a magnifying glass"></div>
  <div class="abs label" style="left:492px;top:1882px">Our Services</div>
  <h2 class="abs h2" style="left:492px;top:1922px;width:520px">Comprehensive Dental Care Tailored to Your Smile</h2>
  <p class="abs body" style="left:492px;top:2006px;width:600px;color:var(--ink);font-size:19px">Experience refined dental care tailored to your needs — combining advanced treatments with comfort, discretion, and exceptional professionalism.</p>

  <div class="svc" style="left:492px;top:2126px"><svg width="44" height="44" viewBox="0 0 24 24" fill="none" stroke="#1e88e5" stroke-width="2" stroke-linejoin="round"><path d="M7 3c-3 0-5 2.5-4 6 .6 2.2 1.6 3.5 2 6 .4 3 1 6 2.5 6s1.8-4 2.5-6c.4-1 1.6-1 2 0 .7 2 1 6 2.5 6s2.1-3 2.5-6c.4-2.5 1.4-3.8 2-6 1-3.5-1-6-4-6-2 0-3 1-5 1S9 3 7 3z"/></svg><div><h4>Cosmetic Dentistry</h4><p>Brighten and enhance your smile with whitening, veneers, and reshaping.</p></div></div>
  <div class="svc" style="left:808px;top:2126px"><svg width="44" height="44" viewBox="0 0 24 24" fill="none" stroke="#1e88e5" stroke-width="2" stroke-linejoin="round"><path d="M7 3c-3 0-5 2.5-4 6 .6 2.2 1.6 3.5 2 6 .4 3 1 6 2.5 6s1.8-4 2.5-6c.4-1 1.6-1 2 0 .7 2 1 6 2.5 6s2.1-3 2.5-6c.4-2.5 1.4-3.8 2-6 1-3.5-1-6-4-6-2 0-3 1-5 1S9 3 7 3z"/></svg><div><h4>Emergency Services</h4><p>Fast treatment for toothaches, broken teeth, and urgent dental issues.</p></div></div>
  <div class="svc" style="left:492px;top:2205px"><svg width="44" height="44" viewBox="0 0 24 24" fill="none" stroke="#1e88e5" stroke-width="2" stroke-linejoin="round"><path d="M7 3c-3 0-5 2.5-4 6 .6 2.2 1.6 3.5 2 6 .4 3 1 6 2.5 6s1.8-4 2.5-6c.4-1 1.6-1 2 0 .7 2 1 6 2.5 6s2.1-3 2.5-6c.4-2.5 1.4-3.8 2-6 1-3.5-1-6-4-6-2 0-3 1-5 1S9 3 7 3z"/></svg><div><h4>Implants</h4><p>Replace missing teeth with strong, natural-looking dental implants.</p></div></div>
  <div class="svc" style="left:808px;top:2205px"><svg width="44" height="44" viewBox="0 0 24 24" fill="none" stroke="#1e88e5" stroke-width="2" stroke-linejoin="round"><path d="M7 3c-3 0-5 2.5-4 6 .6 2.2 1.6 3.5 2 6 .4 3 1 6 2.5 6s1.8-4 2.5-6c.4-1 1.6-1 2 0 .7 2 1 6 2.5 6s2.1-3 2.5-6c.4-2.5 1.4-3.8 2-6 1-3.5-1-6-4-6-2 0-3 1-5 1S9 3 7 3z"/></svg><div><h4>Restorations</h4><p>Repair damaged teeth with quality fillings, crowns, and bridges.</p></div></div>
  <div class="svc" style="left:492px;top:2283px"><svg width="44" height="44" viewBox="0 0 24 24" fill="none" stroke="#1e88e5" stroke-width="2" stroke-linejoin="round"><path d="M7 3c-3 0-5 2.5-4 6 .6 2.2 1.6 3.5 2 6 .4 3 1 6 2.5 6s1.8-4 2.5-6c.4-1 1.6-1 2 0 .7 2 1 6 2.5 6s2.1-3 2.5-6c.4-2.5 1.4-3.8 2-6 1-3.5-1-6-4-6-2 0-3 1-5 1S9 3 7 3z"/></svg><div><h4>Dental Hygiene</h4><p>Keep your teeth and gums healthy with regular cleanings and checkups.</p></div></div>
  <div class="svc" style="left:808px;top:2283px"><svg width="44" height="44" viewBox="0 0 24 24" fill="none" stroke="#1e88e5" stroke-width="2" stroke-linejoin="round"><path d="M7 3c-3 0-5 2.5-4 6 .6 2.2 1.6 3.5 2 6 .4 3 1 6 2.5 6s1.8-4 2.5-6c.4-1 1.6-1 2 0 .7 2 1 6 2.5 6s2.1-3 2.5-6c.4-2.5 1.4-3.8 2-6 1-3.5-1-6-4-6-2 0-3 1-5 1S9 3 7 3z"/></svg><div><h4>Dentures</h4><p>Custom-made dentures for a comfortable, confident smile.</p></div></div>
</section>

<section>
  <div class="abs label center" style="top:2506px">Why Choose Us</div>
  <h2 class="abs h2 center" style="top:2547px">Where Expertise Meets Comfort and Care</h2>
  <p class="abs body center" style="top:2600px;color:var(--ink);font-size:19px">At Maplecrest Dentistry, we combine expert care, advanced technology, and a<br>friendly approach to make you feel confident and comfortable every visit.</p>
  <div class="why-card first" style="left:77px"><h3>Professional</h3><h5>Experienced &amp; Skilled Dentists</h5><p>Our team consists of certified professionals with years of experience, dedicated to providing exceptional dental care with precision and empathy.</p></div>
  <div class="why-card" style="left:429px"><h3>Safe</h3><h5>Safe &amp; Advanced Technology</h5><p>We use modern, sterilized equipment and up-to-date techniques to ensure a safe, hygienic, and effective treatment experience.</p></div>
  <div class="why-card" style="left:781px"><h3>Friendly</h3><h5>Comfort-First Patient Care</h5><p>From the moment you walk in, we focus on your comfort. Our friendly staff is here to make your visit stress-free and pleasant.</p></div>
</section>

<section>
  <div class="abs label center" style="top:3054px">Patient Testimonials</div>
  <h2 class="abs h2 center" style="top:3085px">Comfortable Experience &amp; Trusted Care</h2>
  <p class="abs body center" style="top:3128px;color:var(--ink);font-size:19px">We are proud to have earned the trust of our patients. Here are some real stories<br>from those who have experienced the best care at Maplecrest Dentistry.</p>

  <div class="tcard" style="left:79px;top:3316px;width:269px;height:292px">
    <div class="who" style="left:16px;top:26px;gap:10px"><div class="avatar" style="width:52px;height:52px" role="img" aria-label="Patient portrait"></div><div><b style="font-size:16px">Alina</b><div style="font-size:10px;margin-top:6px">Lead Designer <span class="stars" style="font-size:14px">★★★★☆</span></div></div></div>
    <div style="position:absolute;top:110px;width:100%;font-size:16px;font-weight:700">Absolutely stunning!</div>
    <p style="position:absolute;top:148px;left:20px;right:20px;font-size:11px;line-height:13px;font-style:italic">Their expertise and gentle approach make every visit stress-free. I've never felt more at ease in a dental clinic!</p>
  </div>
  <div class="tcard" style="left:406px;top:3241px;width:379px;height:407px;box-shadow:0 4px 12px rgba(0,0,0,.08)">
    <div class="who" style="left:20px;top:36px;gap:12px"><div class="avatar" style="width:66px;height:66px" role="img" aria-label="Patient portrait"></div><div><b style="font-size:21px">Marcus</b><div style="font-size:16px;margin-top:8px">Lead Designer <span class="stars" style="font-size:22px;margin-left:20px">★★★★☆</span></div></div></div>
    <div style="position:absolute;top:138px;width:100%;font-size:22px;font-weight:600">It was a very good experience</div>
    <p style="position:absolute;top:190px;left:22px;right:22px;font-size:17px;line-height:21px">I always feel very comfortable and confident every time I visit. The team is friendly and professional, and the equipment is impressively modern!</p>
  </div>
  <div class="tcard" style="left:844px;top:3320px;width:268px;height:292px">
    <div class="who" style="left:16px;top:36px;gap:10px"><div class="avatar" style="width:52px;height:52px;background:linear-gradient(135deg,#222,#7a1e2a)" role="img" aria-label="Patient portrait"></div><div><b style="font-size:16px">Devon</b><div style="font-size:10px;margin-top:6px">Lead Designer <span class="stars" style="font-size:14px">★★★★☆</span></div></div></div>
    <div style="position:absolute;top:118px;width:100%;font-size:16px;font-weight:700">High-quality and elegant.</div>
    <p style="position:absolute;top:160px;left:22px;right:22px;font-size:11px;line-height:13px">From the moment I walk in, I'm greeted with warmth and care. The attention to detail and patient comfort here is truly unmatched.</p>
  </div>

  <svg class="abs" style="left:450px;top:3668px" width="20" height="20" viewBox="0 0 20 20"><path d="M13 3 6 10l7 7" fill="none" stroke="#1e88e5" stroke-width="3"/></svg>
  <div class="abs dots"><span class="on"></span><span></span><span></span><span></span><span></span><span></span></div>
  <svg class="abs" style="left:722px;top:3668px" width="20" height="20" viewBox="0 0 20 20"><path d="m7 3 7 7-7 7" fill="none" stroke="#1e88e5" stroke-width="3"/></svg>
</section>

<section>
  <div class="ph map" role="img" aria-label="Street map showing the clinic location and nearby area"></div>
  <div class="abs info">
    <h3><svg width="24" height="24" viewBox="0 0 24 24"><circle cx="12" cy="12" r="11" fill="#fff"/><path d="M12 6v6l4 2" stroke="#1e88e5" stroke-width="2.4" fill="none"/></svg>Opening Hours</h3>
    <ul><li>Monday – Friday: 08:00 AM – 05:00 PM</li><li>Saturday: 08:00 AM – 02:00 PM</li><li>Sunday: Closed</li></ul>
    <h3 style="margin-top:34px"><svg width="22" height="28" viewBox="0 0 22 28"><path d="M11 1C5.5 1 1 5.3 1 10.8 1 18 11 27 11 27s10-9 10-16.2C21 5.3 16.5 1 11 1z" fill="#fff"/><circle cx="11" cy="11" r="4" fill="#1e88e5"/></svg>Contact &amp; Location</h3>
    <div class="addr" style="margin-top:14px">Address</div>
    <ul class="addr" style="margin-top:2px;width:360px"><li>Maplecrest Dentistry 48 Harbor Lane, Suite 2, Brookfield, IL 60513 (Use actual address if available)</li><li>Phone: +1 (555) 010-7391</li><li>Email: contact@maplecrestdentistry.com</li></ul>
  </div>
</section>

<section>
  <div class="ph bottom-band"></div>
  <div class="abs contact-card">
    <div class="field" style="left:464px;top:62px"><label>First Name</label><span>|</span></div>
    <div class="field" style="left:737px;top:62px"><label>Last Name</label><span>Doe</span></div>
    <div class="field" style="left:464px;top:143px"><label>Email</label><span></span></div>
    <div class="field" style="left:737px;top:143px"><label>Phone Number</label><span style="color:#222">+1-555-010-2846</span></div>
    <div class="field" style="left:464px;top:316px;width:513px"><label>Message</label><span>Write your message..</span></div>
    <div class="btn-green" style="position:absolute;left:795px;top:399px;width:182px;height:42px;font-size:14px">Send Message</div>
  </div>
  <div class="abs contact-panel">
    <h3>Contact Information</h3>
    <div class="sub">Say something to start a live chat!</div>
    <div class="cline" style="top:208px"><svg width="20" height="20" viewBox="0 0 24 24"><path d="M6.6 10.8a15 15 0 0 0 6.6 6.6l2.2-2.2c.3-.3.7-.4 1-.2 1.1.4 2.3.6 3.6.6.6 0 1 .4 1 1V20c0 .6-.4 1-1 1A17 17 0 0 1 3 4c0-.6.4-1 1-1h3.5c.6 0 1 .4 1 1 0 1.3.2 2.5.6 3.6.1.3 0 .7-.2 1z" fill="#fff"/></svg>+1-555-010-2846</div>
    <div class="cline" style="top:272px"><svg width="20" height="16" viewBox="0 0 20 16"><rect width="20" height="16" rx="2" fill="#fff"/><path d="m1 2 9 7 9-7" stroke="#1e88e5" stroke-width="1.6" fill="none"/></svg>hello@maplecrestsmiles.com</div>
    <div class="soc" style="left:34px"></div>
    <div class="soc" style="left:80px;background:#fff;border:6px solid #111"></div>
    <div class="soc" style="left:126px"></div>
  </div>
</section>

<footer>
  <div class="ph fline"></div>
  <div class="abs" style="left:79px;top:5150px;color:#fff;font-size:40px;font-weight:600;line-height:1">Maplecrest<div style="font-size:18px;letter-spacing:7px;margin-top:6px">DENTISTRY</div></div>
  <div class="fcol" style="left:383px"><h6>Company</h6><ul><li>About Us</li><li>Why Us</li></ul></div>
  <div class="fcol" style="left:508px"><h6>Legal</h6><ul><li>Privacy Policy</li><li>Terms &amp; Services</li><li>Terms of Use</li><li>Refund Policy</li></ul></div>
  <div class="fcol" style="left:671px"><h6>Quick Links</h6><ul><li>Home</li><li>Services</li><li>Contact</li><li>Book Now</li></ul></div>
  <div class="abs news">
    <h6>Join Our Newsletter</h6>
    <div class="form"><span>Your email address</span><b>Subscribe</b></div>
    <p>* Will send you weekly updates for your better tooth management.</p>
  </div>
  <div class="abs copy center" style="text-align:center">Maplecrest- All Rights Reserved. Copyright © 2025</div>
</footer>

</body>
</html>
```